beauty salon

providing waxing services from a home base this must include which I will provide a price list and an address

Industry/Entity Type

Beauty Salon

Font styles to use
Script

Colors

Designer to choose colors to be used in the design.

```html
<!DOCTYPE html>
<html lang="en">
<head>
<meta charset="utf-8">
<title>Rosalind's Garden Salon – Waxing Price List</title>
<link rel="stylesheet" href="https://fonts.googleapis.com/css2?family=Marcellus&family=Noto+Serif:ital,wght@1,700&family=Open+Sans:ital,wght@0,300;0,700;1,700&family=Arimo&display=swap">
<style>
  :root {
    --page-bg: #e8e5e1;
    --card-bg: #ffffff;
    --plum: #7b2262;
    --plum-edge: #b9b9b9;
    --ink: #2b2b2b;
    --list-ink: #333333;
    --white: #ffffff;
    --bubble-light: #6fb0e4;
    --bubble-dark: #1c5ea8;
    --arc-blue: #2f63b0;
    --footer: #444547;
    --photo-light: #fbf5f1;
    --photo-skin: #e9c3ad;
  }
  * { margin: 0; padding: 0; box-sizing: border-box; }
  html, body { width: 1200px; height: 872px; overflow: hidden; }
  body { background: var(--page-bg); position: relative; }

  .flyer {
    position: absolute; left: 35px; top: 35px;
    width: 1130px; height: 800px;
    background: var(--card-bg); overflow: hidden;
  }
  .flyer-art { position: absolute; inset: 0; }

  .brand {
    position: absolute; left: 60px; top: 96px; width: 440px;
    display: flex; align-items: center; justify-content: center; gap: 12px;
    font-family: "Marcellus", serif; font-size: 31px; color: var(--plum);
  }
  .brand-dot { width: 14px; height: 14px; border-radius: 50%; background: var(--plum); }

  .credential {
    position: absolute; left: 88px; top: 150px;
    font-family: "Open Sans", sans-serif; font-style: italic; font-weight: 700;
    font-size: 15px; color: var(--ink); white-space: nowrap;
  }
  .credential strong { font-style: normal; font-size: 21px; letter-spacing: -0.3px; }

  .hours-band {
    position: absolute; left: 0; top: 197px; width: 655px; height: 168px;
    background: var(--plum);
    border-top: 4px solid var(--plum-edge); border-bottom: 4px solid var(--plum-edge);
    display: flex; flex-direction: column; justify-content: center; align-items: center;
    font-family: "Noto Serif", serif; font-style: italic; font-weight: 700;
    color: var(--white); font-size: 26px; line-height: 35px; padding-right: 50px;
  }

  .offer {
    position: absolute; left: 490px; top: 36px; width: 240px;
    text-align: center; color: var(--white);
    font-family: "Noto Serif", serif; font-style: italic; font-weight: 700;
    text-shadow: 0 1px 2px rgba(0,0,0,.35);
  }
  .offer-amount { font-size: 33px; line-height: 40px; }
  .offer-line { font-size: 23px; line-height: 34px; }
  .offer-line.large { font-size: 25px; }

  .price-list {
    position: absolute;
    font-family: "Arimo", sans-serif; font-size: 14.5px; color: var(--list-ink);
  }
  .price-list h2 {
    font-family: "Noto Serif", serif; font-style: italic; font-weight: 700;
    font-size: 19px; color: var(--ink); text-align: center; margin-bottom: 2px;
  }
  .price-row { display: flex; align-items: baseline; }
  .price-row .dots { flex: 1; border-bottom: 1.5px dotted #555; margin: 0 2px; transform: translateY(-3px); }
  .ladies { left: 33px; top: 378px; width: 219px; }
  .ladies .price-row { height: 20.2px; }
  .mens { left: 293px; top: 378px; width: 219px; }
  .mens .price-row { height: 27.7px; }
  .mens h2 { margin-bottom: 4px; }
  .mens h2.eye-heading { margin-top: 4px; margin-bottom: 4px; }

  .contact-bar {
    position: absolute; left: 0; top: 727px; width: 1130px; height: 73px;
    background: var(--footer); color: var(--white);
    display: flex; align-items: center; padding-left: 90px; gap: 18px;
    font-family: "Open Sans", sans-serif; white-space: nowrap;
  }
  .contact-phone { font-style: italic; font-weight: 700; font-size: 35px; letter-spacing: -0.5px; }
  .contact-address { font-weight: 300; font-size: 39px; letter-spacing: -0.5px; }
</style>
</head>
<body>
<main class="flyer">
  <svg class="flyer-art" width="1130" height="800" viewBox="0 0 1130 800" aria-hidden="false">
    <defs>
      <linearGradient id="photoTone" x1="0" y1="0" x2="1" y2="0.3">
        <stop offset="0" stop-color="var(--photo-light)"/>
        <stop offset="0.55" stop-color="var(--photo-skin)"/>
        <stop offset="1" stop-color="#f3ddd0"/>
      </linearGradient>
      <linearGradient id="arcTone" x1="0" y1="0" x2="0" y2="1">
        <stop offset="0" stop-color="#dfe8f5"/>
        <stop offset="0.4" stop-color="var(--arc-blue)"/>
        <stop offset="1" stop-color="#1f4f98"/>
      </linearGradient>
      <linearGradient id="bubbleTone" x1="0" y1="0" x2="0" y2="1">
        <stop offset="0" stop-color="var(--bubble-light)"/>
        <stop offset="1" stop-color="var(--bubble-dark)"/>
      </linearGradient>
    </defs>
    <path role="img" aria-label="Photo of a woman with clear skin and a white lily tucked behind her ear"
          d="M862 0 C702 110 575 420 605 727 L1130 727 L1130 0 Z" fill="url(#photoTone)"/>
    <path d="M850 0 C690 110 560 420 590 727" fill="none" stroke="url(#arcTone)" stroke-width="7"/>
    <path d="M510 30 H712 Q730 30 730 48 V160 Q730 178 712 178 H560 L505 222 L520 178 H508 Q490 178 490 160 V48 Q490 30 510 30 Z"
          fill="url(#bubbleTone)" stroke="#2a5f9e" stroke-width="2"/>
  </svg>

  <div class="brand"><span class="brand-dot"></span>Rosalind's Garden Salon</div>
  <p class="credential">Diploma of Beauty Therapy &nbsp;At <strong>Mara Quinlan</strong></p>

  <section class="hours-band">
    <p>Now open:</p>
    <p>Wednesday 10am – 4pm</p>
    <p>Fridays 10am-7pm</p>
    <p>Saturday 10am - 4pm</p>
  </section>

  <div class="offer">
    <p class="offer-amount">10% Off</p>
    <p class="offer-line">discount on</p>
    <p class="offer-line large">first treatment</p>
  </div>

  <section class="price-list ladies">
    <h2>Lady’s Waxing</h2>
    <div class="price-row"><span>Eyebrow</span><span class="dots"></span><span>$8</span></div>
    <div class="price-row"><span>Upper lip</span><span class="dots"></span><span>$8</span></div>
    <div class="price-row"><span>Chin</span><span class="dots"></span><span>$8</span></div>
    <div class="price-row"><span>Face wax</span><span class="dots"></span><span>$25</span></div>
    <div class="price-row"><span>Bikini line</span><span class="dots"></span><span>$15</span></div>
    <div class="price-row"><span>G string</span><span class="dots"></span><span>$20</span></div>
    <div class="price-row"><span>½ Brazilian</span><span class="dots"></span><span>$30</span></div>
    <div class="price-row"><span>Full Brazilian</span><span class="dots"></span><span>$40</span></div>
    <div class="price-row"><span>Half arm</span><span class="dots"></span><span>$20</span></div>
    <div class="price-row"><span>Upper half arm</span><span class="dots"></span><span>$20</span></div>
    <div class="price-row"><span>Full arm</span><span class="dots"></span><span>$25</span></div>
    <div class="price-row"><span>Half leg</span><span class="dots"></span><span>$15</span></div>
    <div class="price-row"><span>Upper leg</span><span class="dots"></span><span>$20</span></div>
    <div class="price-row"><span>¾ Leg</span><span class="dots"></span><span>$25</span></div>
    <div class="price-row"><span>Full leg</span><span class="dots"></span><span>$35</span></div>
  </section>

  <section class="price-list mens">
    <h2>Men’s Waxing</h2>
    <div class="price-row"><span>Eyebrow</span><span class="dots"></span><span>$10</span></div>
    <div class="price-row"><span>Half arm</span><span class="dots"></span><span>$20</span></div>
    <div class="price-row"><span>Upper half arm</span><span class="dots"></span><span>$25</span></div>
    <div class="price-row"><span>Full arm</span><span class="dots"></span><span>$30</span></div>
    <div class="price-row"><span>Half leg</span><span class="dots"></span><span>$25</span></div>
    <div class="price-row"><span>Full leg</span><span class="dots"></span><span>$45</span></div>
    <div class="price-row"><span>Chest wax</span><span class="dots"></span><span>$40</span></div>
    <div class="price-row"><span>Back wax</span><span class="dots"></span><span>$35</span></div>
    <h2 class="eye-heading">Eye Enhancement</h2>
    <div class="price-row"><span>Eyebrow tint</span><span class="dots"></span><span>$12</span></div>
    <div class="price-row"><span>Eyelash tint</span><span class="dots"></span><span>$15</span></div>
  </section>

  <footer class="contact-bar">
    <span class="contact-phone">Call us &nbsp;0491 570 156</span>
    <span class="contact-address">12 Finch Lane Oakridge</span>
  </footer>
</main>
</body>
</html>
```